Flyer-Design für Neueröffnung eines Online-Shops
Zielgruppe
Ich verkaufe Online Lebensmittel, die normalerweise entsorgt werden, da das Mindesthaltbarkeitsdatum (MHD ) entweder in Kürze abläuft oder bereits überschritten ist, obwohl diese noch genießbar sind.
Der Fokus liegt auf nicht kühlbedürftige Ware wie Getränke, Süßwaren, Cerealien, Konserven, Gewürze, Getreidetrockenprodukte. Hinzu kommen Sonderposten aus Geschäftsauflösungen, Überproduktionen usw.
Das Ziel ist es, die Lebensmittelverschwendung zu reduzieren und der Bevölkerung, genießbare Lebensmittel zu einem geringen Preis anzubieten.
Die beiden Hauptzielgruppen sind;
1. Umweltbewusste Personen, die die Reduzierung der Lebensmittelverschwendung unterstützen wollen
2. Personen aus dem Niedriglohnsektor, die jeden Euro 'zweimal' umdrehen müssen und sich keine Markenware leisten können.
Aufgabenstellung
Der Onlineshop startet im Januar, das bedeutet der Onlineshop ist noch nicht bekannt. Daher soll der Flyer einem sofort ins Auge fallen. Jedoch soll auf dem Flyer nicht erwähnt werden, dass es sich um einen 'Neueröffnung' handelt.
Jedoch fahre ich eine Eröffnungsaktion, die jedoch als 'Januar' Special' oder Neujahrsspecial' o.ä. betitelt werden soll. Nämlich 'versandkostenfreie Lieferung ab 10€ Warenwert*'
*gilt für Bestellungen bis zum 31.01.18
Folgende Inhalte sollten im Design vorkommen:
Das Logo, der Slogan ' Verschwendung reduzieren, Ersparnis maximieren', die Domain 'www.kor-tibu.de' + der Hinweis auf die versandkostenfreie Lieferung am 10€ Warenwert im Januar.
Folgende Inhalte sind optional:
Stichwörter wie 'nachhaltig', 'umweltbewusst', 'bis zu 70% Ersparnis', '82kg Lebensmittel werden jährlich pro Person entsorgt',
Als Farbton sollte grün im Vordergrund stehen, gerne in zwei verschiedenen Helligkeitsstufen. Als Kontrastfarben wären Ideen rot( für den Rabatt/Ersparnis und da es sich um MHD nahe Lebensmittel handelt ) und schwarz oder weiß.
Der Flyer wird im A5 Hochformat gedruckt ( Querformat bei Bedarf auch möglich ). Dicke = voraussichtlich 300gr (alternativ 250gr ), 2-seitig
Ich werde das Logo und eine erste Skizze von einer Flyervorlage. Die Flyervorlage soll jedoch nur als Unterstützung für die Farbgebung dienen. Bitte die Designs unabhängig davon gestalten und diese evtl als kleine 'Hilfe' nutzen.
Da das Thema recht erklärungsbedürftig ist, ist meine Idee auf der Rückseite eine Art Begriffsklärung zu erstellen. Eine Vorlage für den Inhalt habe ich erstellt und wird ebenfalls hochgeladen. Jedoch soll die Begriffsklärung nicht einfach runtergeschrieben werden sondern kreativ eingebaut/verpackt werden ( z.B. Sprechblasen oder Emojis, Cliparts o.ä. )
Der Kunde soll sofort sehen, dass es darum geht die Lebensmittelverschwendung zu reduzieren und im gleichen Zuge genießb..

```html
<!DOCTYPE html>
<html lang="de">
<head>
<meta charset="utf-8">
<title>KOR Tibu – Januar Special</title>
<link rel="stylesheet" href="https://fonts.googleapis.com/css2?family=Archivo:wght@600;700;800&family=Archivo+Black&display=swap">
<style>
  :root {
    --green-bright: #35bd52;
    --green-mid: #4a8a5a;
    --green-deep-top: #33553b;
    --green-deep-bottom: #456f4e;
    --green-footer: #43963f;
    --red: #ff0010;
    --ink: #111111;
    --white: #ffffff;
  }
  html, body {
    margin: 0;
    padding: 0;
    overflow: hidden;
    background: var(--white);
  }
  .flyer {
    position: relative;
    width: 851px;
    height: 1200px;
    overflow: hidden;
    background: var(--white);
  }
  .flyer-art {
    position: absolute;
    inset: 0;
    width: 851px;
    height: 1200px;
  }
  .footnote { font: 700 15px "Archivo", Arial, sans-serif; fill: var(--ink); }
  .promo { font: 700 38px "Archivo", Arial, sans-serif; fill: var(--white); }
  .slogan { font: 400 62px "Archivo Black", Arial, sans-serif; fill: var(--white); }
  .tagline { font: 800 27px "Archivo", Arial, sans-serif; fill: var(--ink); }
  .category { font: 700 48px "Archivo", Arial, sans-serif; text-anchor: middle; }
  .savings-top, .savings-bottom { font: 400 86px "Archivo Black", Arial, sans-serif; fill: var(--ink); }
  .savings-bottom { font-size: 52px; }
  .savings-figure { font: 800 150px "Archivo", Arial, sans-serif; fill: var(--red); }
  .order-label { font: 700 44px "Archivo", Arial, sans-serif; fill: var(--white); }
  .order-url { font: 800 44px "Archivo", Arial, sans-serif; fill: var(--ink); }
  .brand-name { font: 600 30px "Archivo", Arial, sans-serif; fill: var(--white); text-anchor: middle; }
</style>
</head>
<body>
<div class="flyer">
  <svg class="flyer-art" viewBox="0 0 851 1200" xmlns="http://www.w3.org/2000/svg">
    <defs>
      <linearGradient id="category-fill" x1="0" y1="0" x2="0" y2="1">
        <stop offset="0" stop-color="var(--green-deep-top)"/>
        <stop offset="0.5" stop-color="var(--green-deep-bottom)"/>
        <stop offset="1" stop-color="var(--green-deep-bottom)"/>
      </linearGradient>
    </defs>

    <text class="footnote" x="9" y="22">*gilt für Bestellungen bis zum 31.01.18</text>

    <!-- category panel -->
    <rect class="category-panel" x="37" y="400" width="327" height="508" fill="url(#category-fill)"/>

    <!-- slanted bands -->
    <polygon class="band-promo" points="0,135 851,15 851,86 0,207" fill="var(--green-bright)"/>
    <polygon class="band-slogan" points="0,207 851,86 851,359 0,480" fill="var(--green-mid)"/>

    <g transform="rotate(-8.06 26 180)">
      <text class="promo" x="26" y="180" textLength="790" lengthAdjust="spacingAndGlyphs">JANUAR Special - ab 10 € versandkostenfrei<tspan dy="-18" font-size="26">*</tspan></text>
    </g>

    <g transform="rotate(-8.06 30 294)">
      <text class="slogan" x="30" y="294" textLength="800" lengthAdjust="spacingAndGlyphs">Verschwendung Minimieren,</text>
      <text class="slogan" x="38" y="364" textLength="690" lengthAdjust="spacingAndGlyphs">Ersparnisse maximieren</text>
      <text class="tagline" x="46" y="406" textLength="640" lengthAdjust="spacingAndGlyphs">Der Online shop für MHD nahe Lebensmittel</text>
    </g>

    <!-- categories -->
    <text class="category" x="200" y="533" fill="#a9ada7">Getränke</text>
    <text class="category" x="200" y="602" fill="#cdd0cb">Süßigkeiten</text>
    <text class="category" x="200" y="670" fill="#eceeea">Gewürze</text>
    <text class="category" x="200" y="739" fill="var(--white)">Konserven</text>
    <text class="category" x="200" y="807" fill="var(--white)">Cerialien</text>
    <text class="category" x="200" y="876" fill="var(--white)">Getreide</text>

    <!-- savings badge -->
    <g transform="rotate(11 640 700)">
      <text class="savings-top" x="515" y="585" textLength="285" lengthAdjust="spacingAndGlyphs">BIS ZU</text>
      <text class="savings-figure" x="505" y="720" textLength="240" lengthAdjust="spacingAndGlyphs">70%</text>
      <text class="savings-bottom" x="445" y="775" textLength="335" lengthAdjust="spacingAndGlyphs">ERSPARNISS</text>
    </g>

    <!-- footer -->
    <rect class="footer" x="0" y="1056" width="851" height="144" fill="var(--green-footer)"/>
    <line x1="655.5" y1="1058" x2="655.5" y2="1200" stroke="#3a8537" stroke-width="1"/>
    <text class="order-label" x="21" y="1117" textLength="455" lengthAdjust="spacingAndGlyphs">Online Bestellen auf:</text>
    <text class="order-url" x="25" y="1167" textLength="375" lengthAdjust="spacingAndGlyphs">www.kor-tibu.de</text>

    <rect class="brand-mark" x="728" y="1080" width="50" height="50" fill="var(--white)"/>
    <text class="brand-name" x="753" y="1184">KOR Tibu</text>
  </svg>
</div>
</body>
</html>
```